Marou Cay Lodge Christmas wishes 2013

We require postcards designed to mail our to our clients for Christmas. We are a SURF travel company, with a high end market and like to mail our Christmas postcards to all our guests that have stayed with us through the year. Front cover will have images and text (ie Seasons Greeting) and our logo. The back will have space for TO: name & address and postage stamp. Will also have some basic text (ie The Management & Staff at Marou Cay Lodge wish you and your family all the best for the Festive Season and New Year. We look forward to seeing you back at Marou Cay Lodge again soon etc etc). Here is link to main image https://www.filevault-example.com/sh/qwmzrtpx318kle/Zr8pWnQvcB

Target Market(s)

Our clients are mostly mature men (40-70) surfers who purchase luxury surf trips

Industry/Entity Type

Travel

Requirements
Must have
• Ocean Image (front)
Logo x 2 in same colour - Halcyra & Marou Cay Lodge (front)
Text (front)
Back to be white
Space for name & address (back)
Space for postage stamp (back)
Message (back)
Website www.halcyralodges-example.com (back)

```html
<!DOCTYPE html>
<html lang="en">
<head>
<meta charset="utf-8">
<title>Marou Cay Lodge – Season's Greetings Postcard</title>
<link rel="stylesheet" href="https://fonts.googleapis.com/css2?family=Quicksand:wght@300;400;500;700&display=swap">
<style>
  :root {
    --paper: #ffffff;
    --ink: #4f4f4f;
    --ink-soft: #9a9a9a;
    --rule: #6a6a6a;
    --front-text: #ffffff;
    --glow: #fff7b0;
    --sun: #f7c94c;
    --ember: #e6672f;
    --sea: #b51d17;
    --plum: #55245c;
    --dusk: #3b1a4d;
    --pink: #e44aa0;
  }
  * { margin: 0; padding: 0; box-sizing: border-box; }
  html, body { width: 891px; height: 1200px; overflow: hidden; background: var(--paper); }
  body { font-family: "Quicksand", sans-serif; }
  .postcard { position: relative; width: 891px; height: 1200px; }

  /* Back side */
  .back { position: absolute; inset: 0 0 auto 0; height: 607px; background: var(--paper); }
  .back__website { position: absolute; left: 33px; top: 20px; font-size: 17px; font-weight: 400; color: var(--ink-soft); }
  .back__stamp { position: absolute; left: 752px; top: 37px; width: 101px; height: 127px; border: 1.5px solid var(--rule); }
  .message { position: absolute; left: 250px; top: 92px; width: 380px; }
  .message__quote { position: absolute; font-family: Georgia, serif; font-size: 72px; font-weight: 700; color: var(--ink); line-height: 1; }
  .message__quote--open { left: 2px; top: -16px; }
  .message__quote--close { right: -6px; top: 88px; }
  .message__text { text-align: center; font-size: 19px; line-height: 25px; font-weight: 400; color: var(--ink); padding: 6px 0 0 20px; }
  .message__sign { position: absolute; left: 0; width: 891px; top: 274px; text-align: center; font-size: 13px; color: var(--ink-soft); }
  .address { position: absolute; left: 277px; top: 394px; width: 361px; }
  .address__line { height: 36.5px; border-bottom: 1.5px solid var(--rule); }
  .address__line:first-child { height: 1.5px; }

  /* Front side */
  .front { position: absolute; left: 0; top: 607px; width: 891px; height: 593px; overflow: hidden; }
  .front__photo {
    position: absolute; inset: 0;
    background:
      linear-gradient(to bottom, rgba(0,0,0,0) 0%, rgba(0,0,0,0) 62%, rgba(170,30,20,0.75) 78%, rgba(120,15,20,0.95) 100%),
      radial-gradient(ellipse 70% 45% at 38% 56%, var(--glow) 0%, var(--sun) 28%, var(--ember) 55%, rgba(154,44,90,0.9) 78%, rgba(85,36,92,0) 100%),
      linear-gradient(to bottom, var(--dusk) 0%, var(--plum) 30%, #8a2d5a 55%, var(--sea) 100%);
  }
  .brand { position: absolute; left: 22px; top: 38px; display: flex; align-items: center; gap: 18px; }
  .brand__mark { width: 36px; height: 36px; border-radius: 50%; background: var(--front-text); }
  .brand__name { font-size: 16px; font-weight: 500; letter-spacing: 1.6px; color: var(--front-text); }
  .lodge { position: absolute; right: 40px; top: 25px; width: 160px; text-align: center; color: var(--front-text); }
  .lodge__mark { width: 36px; height: 36px; border-radius: 50%; border: 2px solid var(--front-text); margin: 0 auto 4px; }
  .lodge__name { font-size: 14px; font-weight: 500; }
  .lodge__place { font-size: 12px; font-weight: 500; letter-spacing: 1px; }
  .greeting {
    position: absolute; left: 416px; top: 172px;
    font-size: 52px; font-weight: 300; letter-spacing: -0.5px;
    background: linear-gradient(to right, #fff3f0 0%, #fbc9dc 55%, var(--pink) 100%);
    -webkit-background-clip: text; background-clip: text; color: transparent;
  }
</style>
</head>
<body>
<main class="postcard">
  <section class="back">
    <p class="back__website">www.halcyralodges-example.com</p>
    <div class="back__stamp" aria-label="Postage stamp space"></div>
    <div class="message">
      <span class="message__quote message__quote--open">“</span>
      <p class="message__text">Wish you and your family all the best<br>for the Festive Season and New Year.<br>We look forward to seeing you back at<br>Marou Cay Lodge again soon...</p>
      <span class="message__quote message__quote--close">”</span>
    </div>
    <p class="message__sign">The Management &amp; Staff at Marou Cay Lodge</p>
    <div class="address" aria-label="Recipient name and address">
      <div class="address__line"></div>
      <div class="address__line"></div>
      <div class="address__line"></div>
      <div class="address__line"></div>
    </div>
  </section>

  <section class="front">
    <div class="front__photo" role="img" aria-label="Surfer silhouetted carving a wave against a glowing sunset over the ocean"></div>
    <div class="brand">
      <span class="brand__mark"></span>
      <span class="brand__name">HALCYRA LODGES &amp; RESORTS</span>
    </div>
    <div class="lodge">
      <div class="lodge__mark"></div>
      <p class="lodge__name">maroucaylodge-example.com</p>
      <p class="lodge__place">indonesia</p>
    </div>
    <h1 class="greeting">Season’s Greetings</h1>
  </section>
</main>
</body>
</html>
```